Wine Label

Were looking for a 3.75inch by 7.5 inch one piece wrap wine label. This wine brand is geared toward females and is for a rose, the brand is Salt and Willows, we need space on the label for our story, a barcode, and the government warning. We would like a sleek, sexy label.

```html
<!DOCTYPE html>
<html lang="en">
<head>
<meta charset="utf-8">
<title>Salt &amp; Willows — Rosé Wine Label</title>
<link rel="stylesheet" href="https://fonts.googleapis.com/css2?family=Cormorant+Garamond:wght@400;500&family=Playfair+Display:wght@700&display=swap">
<style>
  :root {
    --backdrop: #1a1a1a;
    --label-black: #070707;
    --label-edge: #141414;
    --copper: #c46a35;
    --copper-dim: #7a3e1f;
    --silver: #c9c9c9;
    --rose-tone: #8f8f8f;
  }
  * { margin: 0; padding: 0; box-sizing: border-box; }
  html, body {
    width: 1200px;
    height: 840px;
    overflow: hidden;
    background: var(--backdrop);
  }
  .canvas {
    position: relative;
    width: 1200px;
    height: 840px;
    display: flex;
    align-items: center;
    justify-content: center;
  }
  .label {
    position: relative;
    width: 760px;
    height: 380px;
    background: linear-gradient(180deg, var(--label-edge) 0%, var(--label-black) 40%, var(--label-black) 100%);
    display: flex;
    align-items: center;
    padding: 0 70px 0 110px;
    gap: 40px;
  }
  .label__text {
    display: flex;
    flex-direction: column;
    align-items: flex-start;
  }
  .winery-name {
    display: flex;
    align-items: center;
    gap: 10px;
    font-family: "Cormorant Garamond", serif;
    font-weight: 500;
    font-size: 20px;
    letter-spacing: 0.32em;
    color: var(--copper-dim);
    margin-bottom: 26px;
  }
  .winery-name__dot {
    width: 8px;
    height: 8px;
    border-radius: 50%;
    background: var(--copper-dim);
  }
  .wine-title {
    font-family: "Playfair Display", serif;
    font-weight: 700;
    font-size: 46px;
    line-height: 1;
    color: var(--copper);
    letter-spacing: 0.01em;
  }
  .wine-type {
    font-family: "Cormorant Garamond", serif;
    font-weight: 400;
    font-size: 40px;
    letter-spacing: 0.06em;
    color: var(--silver);
    margin-top: 8px;
  }
  .wine-details {
    font-family: "Cormorant Garamond", serif;
    font-weight: 500;
    font-size: 14px;
    letter-spacing: 0.08em;
    color: var(--copper-dim);
    margin-top: 14px;
  }
  .rose-illustration {
    flex: none;
    width: 170px;
    height: 230px;
    border-radius: 4px;
    background: linear-gradient(200deg, var(--rose-tone) 0%, #4a4a4a 100%);
    opacity: 0.75;
  }
</style>
</head>
<body>
  <main class="canvas">
    <section class="label">
      <div class="label__text">
        <div class="winery-name"><span class="winery-name__dot"></span>NORTHGATE WINERY</div>
        <h1 class="wine-title">SALT &amp; WILLOWS</h1>
        <p class="wine-type">ROSE WINE</p>
        <p class="wine-details">ALC. 14% BY VOL. 750ML</p>
      </div>
      <div class="rose-illustration" role="img" aria-label="Silver line illustration of a single long-stemmed rose with leaves"></div>
    </section>
  </main>
</body>
</html>
```